Wren's Home Care Retractable Banner Design

Retractable Banner Design
We need a pull up retractable banner design
85 x 206 cm.
We need the banner to use at expo's, information sessions, presentations, recruitment days. Needs to be attractive to our elderly client's and staff (care workers)
Phone number needs to be on 08 6937 4426
Website also needs to be on the banner : wrenshomecare.com.au

Target Market(s)

35 +

Industry/Entity Type

aged care / community

Requirements
Must have
• Colours, fonts and logo as detailed in upload

```html
<!DOCTYPE html>
<html lang="en">
<head>
<meta charset="utf-8">
<title>Wren's Home Care – Pull-up Banner</title>
<link rel="stylesheet" href="https://fonts.googleapis.com/css2?family=Poppins:wght@300;400;600;700;800&family=Oswald:wght@400&display=swap">
<style>
  :root{
    --brand-red:#8c1538;
    --brand-pink:#c8677f;
    --icon-pink:#e892a8;
    --ink:#141414;
    --paper:#ffffff;
    --stage:#e4e6e2;
  }
  *{box-sizing:border-box;margin:0;padding:0}
  html,body{width:1200px;height:1200px;overflow:hidden;background:var(--stage)}
  .banner{
    position:absolute;left:365px;top:30px;width:470px;height:1140px;
    background:var(--paper);overflow:hidden;
    box-shadow:0 6px 24px rgba(0,0,0,.18);
    font-family:"Poppins",sans-serif;color:var(--paper);
  }
  .shape-layer{position:absolute;left:0;top:0;width:470px;height:1140px}
  .photo{
    position:absolute;left:0;top:560px;width:470px;height:380px;
    background:linear-gradient(120deg,#c89a72 0%,#e7d5c8 30%,#5a78c8 52%,#d9d6d8 72%,#8a8fa0 100%);
  }
  .brand-name{
    position:absolute;left:0;top:70px;width:470px;text-align:center;
    font-size:46px;font-weight:400;line-height:1;letter-spacing:.5px;
  }
  .headline{position:absolute;left:0;width:470px;top:196px;text-align:center}
  .headline-lead{font-size:27px;font-weight:600;line-height:1.15}
  .headline-main{font-size:37px;font-weight:700;line-height:1.2;letter-spacing:-.5px}
  .rule{position:absolute;left:30px;right:30px;top:292px;height:2px;background:var(--paper)}
  .intro{position:absolute;left:0;width:470px;top:304px;text-align:center;font-size:16px;font-weight:300;line-height:1.35}
  .intro b,.closing b{font-weight:600}
  .features{position:absolute;left:18px;right:18px;top:362px;display:flex;justify-content:space-between;list-style:none}
  .feature{flex:1;text-align:center;border-left:1.5px dashed rgba(255,255,255,.7)}
  .feature:first-child{border-left:none}
  .feature svg{width:48px;height:48px;display:block;margin:0 auto 8px}
  .feature-label{font-family:"Oswald",sans-serif;font-size:19px;line-height:1.1;text-transform:uppercase}
  .closing{position:absolute;left:0;width:470px;top:476px;text-align:center;font-size:15.5px;font-weight:300;line-height:1.35}
  .badge{position:absolute;border-radius:50%;background:var(--brand-red);text-align:center;color:var(--paper);display:flex;flex-direction:column;justify-content:center;align-items:center}
  .badge-special{left:22px;top:850px;width:112px;height:112px;box-shadow:0 0 0 4px var(--brand-red)}
  .badge-special::before{content:"";position:absolute;inset:5px;border:2px dashed var(--paper);border-radius:50%}
  .badge-special span{font-size:14px;font-weight:800;line-height:1.1}
  .badge-voucher{left:140px;top:812px;width:128px;height:128px;border:4px solid var(--paper)}
  .voucher-pre{font-size:8px;font-weight:400}
  .voucher-amount{font-size:16px;font-weight:800;line-height:1}
  .voucher-note{font-size:5.5px;font-weight:400;line-height:1.2;margin:3px 0}
  .voucher-brand{font-size:7.5px;font-weight:800;line-height:1.1}
  .bottom{position:absolute;left:0;top:975px;width:470px;color:var(--ink)}
  .pitch{position:absolute;left:24px;top:20px;width:180px}
  .pitch-title{color:var(--brand-red);font-size:19px;font-weight:800;line-height:1.1;text-transform:uppercase}
  .pitch-sub{margin-top:12px;font-size:17px;font-weight:600;line-height:1.15}
  .divider{position:absolute;left:210px;top:10px;width:1.5px;height:130px;border-left:1.5px dashed #888}
  .contact{position:absolute;left:224px;top:14px;width:240px}
  .contact-cta{color:var(--brand-red);font-size:13.5px;font-weight:700;line-height:1.15;text-transform:uppercase}
  .contact-phone{display:flex;align-items:center;gap:4px;font-size:33px;font-weight:800;line-height:1.15;letter-spacing:-.5px}
  .contact-phone svg{width:18px;height:18px;flex:none}
  .contact-email{display:flex;align-items:center;gap:5px;font-size:11px;font-weight:600}
  .contact-email svg{width:11px;height:9px;flex:none}
  .contact-web{font-size:14.5px;font-weight:700;margin-top:2px}
  .contact-web em{font-style:normal;color:var(--brand-red)}
</style>
</head>
<body>
<main class="banner">
  <div class="photo" role="img" aria-label="Photo of a smiling care worker in a blue uniform embracing a happy elderly woman at home"></div>

  <svg class="shape-layer" viewBox="0 0 470 1140" aria-hidden="true">
    <defs>
      <linearGradient id="redFade" x1="0" y1="0" x2="0" y2="1">
        <stop offset="0" stop-color="#931a3d"/>
        <stop offset="1" stop-color="#86133a"/>
      </linearGradient>
    </defs>
    <path d="M0 0 H470 V578 Q250 612 0 632 Z" fill="var(--paper)"/>
    <path d="M0 0 H470 V560 Q250 598 0 616 Z" fill="var(--brand-pink)"/>
    <path d="M0 0 H470 V542 Q250 580 0 596 Z" fill="url(#redFade)"/>
    <path d="M0 890 L470 840 V856 L0 906 Z" fill="var(--brand-pink)"/>
    <path d="M0 906 L470 856 V1140 H0 Z" fill="var(--paper)"/>
  </svg>

  <header class="brand-name">Wren's Home Care</header>

  <section class="headline">
    <p class="headline-lead">Do you have a</p>
    <h1 class="headline-main">Home Care Package?</h1>
  </section>
  <div class="rule"></div>
  <p class="intro">We are a home care provider in<br><b>Australia</b> providing services to <b>older people,</b></p>

  <ul class="features">
    <li class="feature">
      <svg viewBox="0 0 48 48" fill="none" stroke="var(--icon-pink)" stroke-width="2.5" stroke-linecap="round" stroke-linejoin="round">
        <circle cx="26" cy="14" r="10"/><path d="M21 14l4 4 7-8"/>
        <path d="M4 38h8l8 3h12l12-9-4-2-9 5H25l-5-6H12"/>
      </svg>
      <div class="feature-label">Convenient<br>Services</div>
    </li>
    <li class="feature">
      <svg viewBox="0 0 48 48" fill="none" stroke="var(--icon-pink)" stroke-width="2.5" stroke-linecap="round">
        <circle cx="20" cy="24" r="18" fill="var(--icon-pink)" fill-opacity=".35"/>
        <path d="M32 18a8 8 0 0 1 0 12M37 14a14 14 0 0 1 0 20"/>
      </svg>
      <div class="feature-label">Your Voice<br>Matters</div>
    </li>
    <li class="feature">
      <svg viewBox="0 0 48 48" fill="none" stroke="var(--icon-pink)" stroke-width="2.5" stroke-linecap="round" stroke-linejoin="round">
        <circle cx="22" cy="26" r="16"/><path d="M14 34L40 8M28 8h12v12"/>
      </svg>
      <div class="feature-label">Seamless<br>Tranistion</div>
    </li>
    <li class="feature">
      <svg viewBox="0 0 48 48" fill="none" stroke="var(--icon-pink)" stroke-width="2.5" stroke-linecap="round" stroke-linejoin="round">
        <circle cx="20" cy="14" r="10"/><circle cx="20" cy="14" r="5"/>
        <path d="M20 14v16l-4-3-3 3 8 12h14l3-12-10-4" fill="var(--icon-pink)" fill-opacity=".35"/>
      </svg>
      <div class="feature-label">Easy to<br>Reach</div>
    </li>
  </ul>

  <p class="closing">Choosing your Home Care Provider is an<br>important decision and at <b>Wren's Care Provider,</b><br>we make switching <b>easy</b> and <b>stress free.</b></p>

  <div class="badge badge-special"><span>SPECIAL<br>REFERRAL<br>OFFER</span></div>
  <div class="badge badge-voucher">
    <span class="voucher-pre">RECEIVE</span>
    <span class="voucher-amount">A $100<br>VOUCHER</span>
    <span class="voucher-note">IF YOU REFER A CLIENT<br>OR CARE WORKER<br>WHO JOINS</span>
    <span class="voucher-brand">WREN'S HOME<br>CARE</span>
  </div>

  <section class="bottom">
    <div class="pitch">
      <p class="pitch-title">Switching providers is easy...</p>
      <p class="pitch-sub">You Deserve<br>the Best Care !</p>
    </div>
    <div class="divider"></div>
    <div class="contact">
      <p class="contact-cta">Call today to chat with<br>our friendly team</p>
      <p class="contact-phone">
        <svg viewBox="0 0 24 24"><path fill="var(--brand-red)" d="M6.6 10.8a15 15 0 0 0 6.6 6.6l2.2-2.2a1 1 0 0 1 1-.25 11.4 11.4 0 0 0 3.6.57 1 1 0 0 1 1 1V20a1 1 0 0 1-1 1A17 17 0 0 1 3 4a1 1 0 0 1 1-1h3.5a1 1 0 0 1 1 1c0 1.25.2 2.45.57 3.57a1 1 0 0 1-.25 1z"/></svg>
        08 6937 4426
      </p>
      <p class="contact-email">
        <svg viewBox="0 0 22 18"><rect x="1" y="1" width="20" height="16" fill="none" stroke="var(--brand-red)" stroke-width="2"/><path d="M1 1l10 8 10-8" fill="none" stroke="var(--brand-red)" stroke-width="2"/></svg>
        enquiries@wrenshomecare.com.au
      </p>
      <p class="contact-web">www.<em>wrenshomecare</em>.com.au</p>
    </div>
  </section>
</main>
</body>
</html>
```